WardPeak landing page

The existing website at www.wardpeak-example.com needs updating. I've attached some marketing material for the color scheme to be used and potential content. The tagline should be "Real-Time Operational Intelligence." I want the landing page to be in 3 categories in this order and features within each category. Plenty of images are preferred and wording can be modified.
Wardpeak Command Centre
- Live Incident tracking and reporting with escalation on critical incidents if necessary
- Geofence Monitoring to ensure guards at the right location at the right time.
- Smart scheduling to ensure the correct training and certifications are assigned to the appropriate guard required.
- Camera compatibility to capture live and historical video for incident reporting
WardPeak Back Office Administration
- Automate Police report filing using data from submitted incidents when required.
- Track all required KPIs on a per site basis such as vehicle inspections, patrol tour details, etc
- Payroll and Invoicing using smart shift reports
- Create and manage client sites with configurable geofencing
WardPeak App
- Guard can see all site details and instructions when logging onto shift
- Ability to view all incidents that have occured at that particular site over the last 'x' days. Understand what has been happening and when.
- Report incidents with all relevant information including photo and video
- Recieve alerts when repeat offences are occuring within a configurable vicinity.

Target Market(s)

Retailers and guard companies

Coding

Coded - Design and coding required

Number of Pages Required

1 page

Requirements
Nice to have
• Use the look and feel of the logo in the design

```html
<!DOCTYPE html>
<html lang="en">
<head>
<meta charset="utf-8">
<title>WardPeak – Unified Security Intelligence</title>
<link href="https://fonts.googleapis.com/css2?family=Manrope:wght@400;500;600;700;800&display=swap" rel="stylesheet">
<style>
:root{
  --brand:#0a9be8;
  --brand-soft:#e6f5fd;
  --ink:#0f1b26;
  --ink-2:#3b4954;
  --muted:#7b8791;
  --line:#e7ecf1;
  --tint:#f5f8fb;
  --panel:#2a3a42;
  --panel-2:#34464f;
  --danger:#e0524f;
  --danger-soft:#fdeeee;
  --white:#fff;
}
*{box-sizing:border-box;margin:0;padding:0}
html,body{width:1200px;height:3534px;overflow:hidden}
body{font-family:"Manrope",sans-serif;color:var(--ink);background:var(--white);position:relative}
.abs{position:absolute}
.label{font-size:7.5px;font-weight:700;letter-spacing:.08em;color:var(--brand);text-transform:uppercase}
.btn{display:flex;align-items:center;justify-content:center;border-radius:5px;font-weight:700;font-size:11px}
.btn-primary{background:var(--brand);color:var(--white)}
.btn-outline{border:1.5px solid var(--brand);color:var(--brand);background:var(--white)}
.btn-ghost{border:1px solid var(--line);color:var(--ink);background:var(--white)}
.icon{width:16px;height:16px;stroke:var(--brand);fill:none;stroke-width:1.6;stroke-linecap:round;stroke-linejoin:round}

/* nav */
.nav{left:0;top:0;width:1200px;height:46px;border-bottom:1px solid var(--line)}
.brand{display:flex;align-items:center;gap:6px;font-weight:800;font-size:11px;color:var(--ink)}
.brand-mark{width:12px;height:12px;border-radius:3px;background:var(--brand)}
.nav-links{left:454px;top:17px;display:flex;gap:22px;font-size:9px;font-weight:600;color:var(--ink-2)}
.nav-login{left:870px;top:17px;font-size:9px;font-weight:600}
.nav-cta{left:913px;top:11px;width:87px;height:24px;font-size:8.5px;border-radius:4px}

/* hero */
.badge{left:526px;top:96px;width:148px;height:15px;border-radius:8px;background:var(--brand-soft);border:1px solid #cbe9fb;color:var(--brand);font-size:6.5px;font-weight:800;display:flex;align-items:center;justify-content:center;gap:5px;letter-spacing:.04em}
.badge i{width:4px;height:4px;border-radius:50%;background:var(--brand)}
.hero-title{left:0;width:1200px;top:128px;text-align:center;font-size:45px;font-weight:700;line-height:47px;letter-spacing:-.02em}
.hero-sub{left:390px;width:420px;top:238px;text-align:center;font-size:11px;line-height:18.5px;color:var(--ink-2)}
.dash{left:281px;top:410px;width:636px;height:359px;border-radius:8px;background:var(--white);box-shadow:0 10px 30px rgba(15,27,38,.15);padding:5px}
.dash-screen{width:100%;height:100%;border-radius:5px;background:radial-gradient(ellipse at 40% 30%,#4d6a72 0%,#2c4148 45%,#1b2a30 100%)}
.alert-card{left:302px;top:428px;width:159px;height:55px;background:var(--white);border-radius:5px;box-shadow:0 6px 18px rgba(0,0,0,.2);padding:9px 11px}
.alert-card .label{font-size:6px;color:var(--brand)}
.alert-dot{right:10px;top:11px;width:5px;height:5px;border-radius:50%;background:var(--danger)}
.alert-row{display:flex;gap:7px;margin-top:8px;align-items:center}
.alert-row strong{display:block;font-size:7.5px;font-weight:700}
.alert-row span{font-size:6px;color:var(--muted)}

/* command */
.sec-title{font-size:23px;font-weight:700;line-height:28px;letter-spacing:-.01em}
.feat{width:157px;height:110px;background:var(--white);border-radius:6px;box-shadow:0 3px 12px rgba(15,27,38,.08);border:1px solid #f0f3f6;padding:17px 15px}
.feat h4{font-size:8.5px;font-weight:700;margin:11px 0 5px}
.feat p{font-size:7px;line-height:11px;color:var(--muted)}
.globe{left:620px;top:939px;width:329px;height:329px;background:radial-gradient(circle at 50% 48%,#6a7479 0%,#4a545a 35%,#394247 70%,#323a3f 100%)}
.acc-card{left:653px;top:1057px;width:263px;height:93px;background:var(--white);border-radius:5px;box-shadow:0 6px 20px rgba(0,0,0,.2);padding:15px 15px}
.acc-ic{width:24px;height:24px;border-radius:5px;background:var(--brand-soft);display:flex;align-items:center;justify-content:center}
.bar{height:3px;border-radius:2px;background:#e8eef2;margin-top:7px}
.bar i{display:block;height:100%;width:95%;border-radius:2px;background:var(--brand)}

/* back office */
.tint{left:0;top:1357px;width:1200px;height:353px;background:var(--tint)}
.ofc{width:162px;height:118px;background:var(--white);border-radius:6px;box-shadow:0 3px 12px rgba(15,27,38,.07);padding:16px 15px}
.ofc h4{font-size:9px;font-weight:700;margin:10px 0 7px}
.ofc p{font-size:7.5px;line-height:14px;color:var(--muted)}

/* field app */
.glow{border-radius:50%;background:radial-gradient(circle,rgba(10,155,232,.12) 0%,rgba(10,155,232,0) 70%)}
.phone{left:322px;top:1770px;width:180px;height:362px;border:5px solid #2c3a44;border-radius:24px;background:var(--white);box-shadow:0 10px 26px rgba(15,27,38,.18);padding:18px 14px}
.ph-head{display:flex;justify-content:space-between;font-size:8px;font-weight:700}
.ph-card{border-radius:5px;margin-top:9px;padding:8px}
.ph-login{background:#f2f9fe;border:1px solid #d5ecfb}
.ph-login .label{font-size:5.5px}
.ph-login strong{display:block;font-size:7px;margin:3px 0 2px}
.ph-login span{font-size:5.5px;color:var(--muted)}
.ph-hist{border:1px solid var(--line);font-size:5.5px;color:var(--muted)}
.ph-bars{display:flex;gap:5px;margin-top:6px}
.ph-bars i{height:2px;flex:1;background:#eceff2;border-radius:1px}
.ph-bars i.r{background:var(--danger)}
.ph-alert{background:var(--danger-soft);border:1px solid #f7d5d4;color:var(--danger);font-size:5.5px}
.ph-alert b{font-size:5.5px;font-weight:800}
.ph-ev{border:1px solid var(--line);font-size:5.5px;font-weight:700}
.ph-drop{height:60px;border:1px solid var(--line);border-radius:4px;margin-top:7px;display:flex;align-items:center;justify-content:center}
.ph-btn{height:22px;margin-top:10px;border-radius:5px;background:var(--brand);color:var(--white);font-size:6.5px;font-weight:800;display:flex;align-items:center;justify-content:center}
.app-item{display:flex;gap:11px;width:330px}
.app-item h5{font-size:9px;font-weight:700;margin-bottom:2px}
.app-item p{font-size:7.5px;line-height:12px;color:var(--muted)}

/* predictive */
.pred-item{display:flex;gap:18px;width:340px}
.pred-ic{width:25px;height:25px;border-radius:50%;background:var(--brand-soft);display:flex;align-items:center;justify-content:center;flex:none}
.pred-item h5{font-size:11.5px;font-weight:700;margin-bottom:4px}
.pred-item p{font-size:9px;line-height:15px;color:var(--muted)}
.engine{left:616px;top:2332px;width:333px;height:299px;background:var(--panel);border-radius:6px;padding:20px 20px}
.engine .label{font-size:6.5px;color:#3bb4f0}
.live{right:20px;top:21px;font-size:6px;color:#4fd0a0;display:flex;gap:4px;align-items:center}
.live i{width:4px;height:4px;border-radius:50%;background:#4fd0a0}
.stats{left:20px;right:20px;bottom:22px;border-top:1px solid #5a6b73;padding-top:22px;display:flex}
.stats div{flex:1}
.stats span{display:block;font-size:5.5px;color:#9fb0b8;font-weight:700;letter-spacing:.05em}
.stats b{font-size:12px;color:var(--white);font-weight:700}

/* ecosystem */
.eco{width:162px;height:90px;background:var(--white);border-radius:6px;border:1px solid #eff2f5;box-shadow:0 3px 12px rgba(15,27,38,.06);display:flex;flex-direction:column;align-items:center;justify-content:center;gap:12px;font-size:9px;font-weight:600;color:var(--ink-2)}
.eco .icon{stroke:#6b7680;width:20px;height:20px}

/* cta */
.cta{left:250px;top:3075px;width:699px;height:266px;border-radius:16px;border:1px solid #eef2f5;background:linear-gradient(120deg,#fff 0%,#fbfcfd 55%,#eef6fc 100%);box-shadow:0 3px 14px rgba(15,27,38,.05)}

/* footer */
.footer{left:0;top:3453px;width:1200px;height:81px;background:var(--tint);border-top:1px solid var(--line)}
.foot-links{left:369px;top:37px;display:flex;gap:20px;font-size:8px;color:var(--ink-2);font-weight:500}
.copy{right:200px;top:37px;font-size:7.5px;color:#a7b1b9}
</style>
</head>
<body>

<header class="nav abs">
  <div class="brand abs" style="left:228px;top:15px"><span class="brand-mark"></span>WardPeak</div>
  <nav class="nav-links abs"><span>Platform</span><span>Intelligence</span><span>Ecosystem</span><span>Pricing</span></nav>
  <span class="nav-login abs">Login</span>
  <span class="btn btn-primary nav-cta abs">Request Demo</span>
</header>

<section>
  <div class="badge abs"><i></i>AI-POWERED SECURITY PLATFORM</div>
  <h1 class="hero-title abs">Unified Security<br>Intelligence</h1>
  <p class="hero-sub abs">Empower your enterprise with a full-stack security ecosystem. From real-time Command Centres to automated Back Office administration and field-ready applications.</p>
  <span class="btn btn-primary abs" style="left:440px;top:317px;width:177px;height:38px">Request Enterprise Demo</span>
  <span class="btn btn-outline abs" style="left:627px;top:317px;width:133px;height:38px">Explore Platform</span>
  <div class="dash abs"><div class="dash-screen" role="img" aria-label="Command centre dashboard on a laptop screen showing a world map, bar charts and live data panels"></div></div>
  <div class="alert-card abs">
    <div class="label">Live Incidents</div><span class="alert-dot abs"></span>
    <div class="alert-row">
      <svg width="10" height="10" viewBox="0 0 10 10"><path d="M5 1 9 5 5 9 1 5Z" fill="none" stroke="#e0524f" stroke-width="1.2"/></svg>
      <div><strong>Critical Escalation</strong><span>Sector 7 Response Required</span></div>
    </div>
  </div>
</section>

<section>
  <div class="label abs" style="left:250px;top:911px">Unified Command Centre</div>
  <h2 class="sec-title abs" style="left:250px;top:931px">Total Visibility Over Your<br>Mission-Critical Operations</h2>
  <p class="abs" style="left:250px;top:1003px;width:330px;font-size:10.5px;line-height:18px;color:var(--ink-2)">A centralized intelligence hub providing complete control over live events, personnel, and integrated hardware assets.</p>
  <div class="feat abs" style="left:250px;top:1060px">
    <svg class="icon" viewBox="0 0 16 16"><path d="M2 14h12M4 11V9M7 11V7M10 11V8M13 11V4M3 7l4-3 3 2 4-4"/></svg>
    <h4>Live Incident Tracking</h4><p>Real-time reporting with critical escalation workflows for immediate response.</p>
  </div>
  <div class="feat abs" style="left:422px;top:1060px">
    <svg class="icon" viewBox="0 0 16 16"><circle cx="8" cy="8" r="5"/><path d="M8 1v2M8 13v2M1 8h2M13 8h2"/></svg>
    <h4>Geofence Monitoring</h4><p>High-precision tracking for guard location accuracy and boundary compliance.</p>
  </div>
  <div class="feat abs" style="left:250px;top:1187px">
    <svg class="icon" viewBox="0 0 16 16"><rect x="2" y="3" width="12" height="11" rx="1.5"/><path d="M2 6h12M5 1.5v3M11 1.5v3M6 10l1.5 1.5L10.5 8.5"/></svg>
    <h4>Smart Scheduling</h4><p>AI-driven scheduling based on specific training, certifications, and availability.</p>
  </div>
  <div class="feat abs" style="left:422px;top:1187px">
    <svg class="icon" viewBox="0 0 16 16"><rect x="1.5" y="4" width="9.5" height="8" rx="1.5"/><path d="M11 7l3.5-2v6L11 9"/></svg>
    <h4>Camera Compatibility</h4><p>Seamless integration for both live streaming and historical video playback.</p>
  </div>
  <div class="globe abs" role="img" aria-label="Dark digital globe with a network grid overlay"></div>
  <div class="acc-card abs">
    <div style="display:flex;gap:10px;align-items:center">
      <div class="acc-ic"><svg class="icon" style="width:11px;height:11px" viewBox="0 0 16 16"><path d="M8 1.5 13.5 3.5v4.5c0 3.2-2.4 5.5-5.5 6.5C4.9 13.5 2.5 11.2 2.5 8V3.5Z"/><circle cx="8" cy="7.5" r="1.8"/></svg></div>
      <div><div style="font-size:9px;font-weight:700">Operational Accuracy</div><div style="font-size:6px;color:var(--muted)">Geofence Status: <span style="color:var(--brand);font-weight:700">Active</span></div></div>
    </div>
    <div style="display:flex;justify-content:space-between;margin-top:16px;font-size:7px;color:var(--muted)"><span>Position Delta</span><span style="color:var(--brand);font-weight:700">± 1.5m</span></div>
    <div class="bar"><i></i></div>
  </div>
</section>

<section>
  <div class="tint abs"></div>
  <div class="label abs" style="left:0;width:1200px;text-align:center;top:1420px">Back Office Administration</div>
  <h2 class="sec-title abs" style="left:0;width:1200px;text-align:center;top:1436px">Streamlined Operational Logistics</h2>
  <p class="abs" style="left:0;width:1200px;text-align:center;top:1475px;font-size:9.5px;color:var(--ink-2)">Automate administrative overhead with smart reporting and financial integration.</p>
  <div class="ofc abs" style="left:250px;top:1530px">
    <svg class="icon" viewBox="0 0 16 16"><path d="M8 1.5 13.5 3.5v4.5c0 3.2-2.4 5.5-5.5 6.5C4.9 13.5 2.5 11.2 2.5 8V3.5Z"/><circle cx="8" cy="7.5" r="1.6"/></svg>
    <h4>Police Reporting</h4><p>Automated Police report filing workflows to save hours of manual documentation.</p>
  </div>
  <div class="ofc abs" style="left:429px;top:1530px">
    <svg class="icon" viewBox="0 0 16 16"><path d="M2 13l4-5 3 3 5-6M10 5h4v4"/></svg>
    <h4>Per-Site KPI</h4><p>Detailed tracking for vehicle inspections, patrol frequency, and site health scores.</p>
  </div>
  <div class="ofc abs" style="left:607px;top:1530px">
    <svg class="icon" viewBox="0 0 16 16"><rect x="1.5" y="4" width="13" height="8" rx="1.5"/><circle cx="8" cy="8" r="2"/></svg>
    <h4>Payroll &amp; Invoicing</h4><p>Financial processing generated directly via smart shift reports and verified logs.</p>
  </div>
  <div class="ofc abs" style="left:786px;top:1530px">
    <svg class="icon" viewBox="0 0 16 16"><rect x="2" y="4" width="7" height="10"/><rect x="9" y="7" width="5" height="7"/><path d="M4 7h3M4 10h3"/></svg>
    <h4>Site Management</h4><p>Comprehensive client site management with integrated geofencing parameters.</p>
  </div>
</section>

<section>
  <div class="glow abs" style="left:420px;top:1830px;width:260px;height:260px"></div>
  <div class="phone abs">
    <div class="ph-head"><span>Site Briefing</span><svg class="icon" style="width:9px;height:9px" viewBox="0 0 16 16"><path d="M8 1.5 13.5 3.5v4.5c0 3.2-2.4 5.5-5.5 6.5C4.9 13.5 2.5 11.2 2.5 8V3.5Z"/></svg></div>
    <div class="ph-card ph-login"><div class="label">On Login</div><strong>Main Lobby Post</strong><span>Instructions: Check ID badges...</span></div>
    <div class="ph-card ph-hist">◷&nbsp; Incident History (Last 7 Days)<div class="ph-bars"><i class="r"></i><i></i><i class="r"></i></div></div>
    <div class="ph-card ph-alert"><div style="display:flex;justify-content:space-between"><b>REPEAT OFFENDER</b><span>⚠</span></div><div style="margin-top:3px;line-height:8px">Proximity alert: Tagged individual within 50m.</div></div>
    <div class="ph-card ph-ev">▣&nbsp; Attach Evidence
      <div class="ph-drop"><svg class="icon" style="stroke:#a7b1b9;width:12px;height:12px" viewBox="0 0 16 16"><rect x="2" y="3" width="12" height="10" rx="1"/><path d="M2 11l4-4 3 3 2-2 3 3"/></svg></div>
    </div>
    <div class="ph-btn">REPORT INCIDENT</div>
  </div>

  <div class="label abs" style="left:624px;top:1787px">WardPeak Field App</div>
  <h2 class="sec-title abs" style="left:624px;top:1806px">Elite Field Intelligence</h2>
  <p class="abs" style="left:624px;top:1850px;width:330px;font-size:10.5px;line-height:18px;color:var(--ink-2)">A high-performance application designed for the front line, ensuring guards have every piece of intelligence they need.</p>
  <div class="app-item abs" style="left:624px;top:1927px">
    <svg class="icon" style="width:14px;height:14px;flex:none" viewBox="0 0 16 16"><circle cx="8" cy="8" r="6"/><path d="M8 7.5v4M8 5v.2"/></svg>
    <div><h5>On-Login Instructions</h5><p>Instant access to site details and post orders immediately upon shift start.</p></div>
  </div>
  <div class="app-item abs" style="left:624px;top:1982px">
    <svg class="icon" style="width:14px;height:14px;flex:none" viewBox="0 0 16 16"><path d="M2 8a6 6 0 1 0 2-4.5M2 2v3h3M8 5v3l2 2"/></svg>
    <div><h5>Site Incident History</h5><p>Review historical data from the last X days to understand recent site patterns.</p></div>
  </div>
  <div class="app-item abs" style="left:624px;top:2037px">
    <svg class="icon" style="width:14px;height:14px;flex:none" viewBox="0 0 16 16"><rect x="1.5" y="4" width="9.5" height="8" rx="1.5"/><path d="M11 7l3.5-2v6L11 9"/></svg>
    <div><h5>Photo &amp; Video Evidence</h5><p>Full multimedia incident reporting for indisputable documentation.</p></div>
  </div>
  <div class="app-item abs" style="left:624px;top:2079px">
    <svg class="icon" style="width:14px;height:14px;flex:none" viewBox="0 0 16 16"><path d="M4 11V7a4 4 0 0 1 8 0v4l1 1.5H3ZM6.5 14h3"/></svg>
    <div><h5>Proximity Alerts</h5><p>Early warning system for repeat offenders detected near site perimeters.</p></div>
  </div>
</section>

<section>
  <div class="glow abs" style="left:470px;top:2160px;width:260px;height:220px;opacity:.6"></div>
  <div class="label abs" style="left:0;width:1200px;text-align:center;top:2253px">Neural Intelligence</div>
  <h2 class="abs" style="left:0;width:1200px;text-align:center;top:2270px;font-size:29px;font-weight:700;letter-spacing:-.01em">Predictive Security Ecosystem</h2>
  <div class="pred-item abs" style="left:256px;top:2418px">
    <div class="pred-ic"><svg class="icon" style="width:11px;height:11px" viewBox="0 0 16 16"><path d="M8 15s5-4.5 5-8.5a5 5 0 0 0-10 0C3 10.5 8 15 8 15Z"/><circle cx="8" cy="6.5" r="1.8"/></svg></div>
    <div><h5>Predictive Risk Scoring</h5><p>Our algorithms analyze historical patterns to predict potential breaches before they occur.</p></div>
  </div>
  <div class="pred-item abs" style="left:256px;top:2493px">
    <div class="pred-ic"><svg class="icon" style="width:11px;height:11px" viewBox="0 0 16 16"><path d="M2 12l4-5 3 3 5-6M10 4h4v4"/></svg></div>
    <div><h5>Autonomous Threat Analysis</h5><p>Instantly classify threats with integrated computer vision across your perimeter.</p></div>
  </div>
  <div class="engine abs">
    <div class="label">Predictive Engine Live</div>
    <div class="live abs"><i></i>Active Monitoring</div>
    <svg class="abs" style="left:106px;top:70px" width="122" height="122" viewBox="0 0 122 122">
      <circle cx="61" cy="61" r="59" fill="none" stroke="#43565f" stroke-width="1.5"/>
      <circle cx="61" cy="61" r="40" fill="none" stroke="#3b4d56" stroke-width="1"/>
      <g fill="#2fa8ea">
        <circle cx="55" cy="52" r="1.3"/><circle cx="61" cy="52" r="1.3"/><circle cx="67" cy="52" r="1.3"/>
        <circle cx="52" cy="57" r="1.3"/><circle cx="58" cy="57" r="1.3"/><circle cx="64" cy="57" r="1.3"/><circle cx="70" cy="57" r="1.3"/>
        <circle cx="49" cy="62" r="1.3"/><circle cx="55" cy="62" r="1.3"/><circle cx="61" cy="62" r="1.3"/><circle cx="67" cy="62" r="1.3"/><circle cx="73" cy="62" r="1.3"/>
        <circle cx="52" cy="67" r="1.3"/><circle cx="58" cy="67" r="1.3"/><circle cx="64" cy="67" r="1.3"/><circle cx="70" cy="67" r="1.3"/>
        <circle cx="55" cy="72" r="1.3"/><circle cx="61" cy="72" r="1.3"/><circle cx="67" cy="72" r="1.3"/>
      </g>
    </svg>
    <div class="stats abs"><div><span>ANOMALY DETECTION</span><b>0.03%</b></div><div><span>LEARNING RATE</span><b>99.2%</b></div></div>
  </div>
</section>

<section>
  <div class="label abs" style="left:0;width:1200px;text-align:center;top:2754px">The Ecosystem</div>
  <h2 class="sec-title abs" style="left:0;width:1200px;text-align:center;top:2772px">Integrated Infrastructure</h2>
  <p class="abs" style="left:0;width:1200px;text-align:center;top:2811px;font-size:9.5px;color:var(--muted)">Native compatibility with enterprise hardware and law enforcement agencies.</p>
  <div class="eco abs" style="left:250px;top:2865px"><svg class="icon" viewBox="0 0 16 16"><rect x="1.5" y="4" width="9.5" height="8" rx="1"/><path d="M11 7l3.5-2v6L11 9"/></svg>CCTV / VMS</div>
  <div class="eco abs" style="left:429px;top:2865px"><svg class="icon" viewBox="0 0 16 16"><circle cx="8" cy="8" r="6"/><circle cx="8" cy="8" r="2.5"/><path d="M8 2v3.5"/></svg>Body Cams</div>
  <div class="eco abs" style="left:607px;top:2865px"><svg class="icon" viewBox="0 0 16 16"><path d="M8 1.5 13.5 3.5v4.5c0 3.2-2.4 5.5-5.5 6.5C4.9 13.5 2.5 11.2 2.5 8V3.5Z"/><path d="M8 5.5l.8 1.6 1.7.2-1.2 1.2.3 1.7L8 9.4l-1.6.8.3-1.7-1.2-1.2 1.7-.2Z"/></svg>Police Systems</div>
  <div class="eco abs" style="left:786px;top:2865px"><svg class="icon" viewBox="0 0 16 16"><circle cx="8" cy="8" r="1.2"/><path d="M5.5 5.5a3.5 3.5 0 0 0 0 5M10.5 5.5a3.5 3.5 0 0 1 0 5M3.2 3.2a6.8 6.8 0 0 0 0 9.6M12.8 3.2a6.8 6.8 0 0 1 0 9.6"/></svg>IoT Sensors</div>
</section>

<section>
  <div class="cta abs"></div>
  <h2 class="abs" style="left:0;width:1200px;text-align:center;top:3123px;font-size:35px;font-weight:700;letter-spacing:-.02em">Ready to secure your enterprise?</h2>
  <p class="abs" style="left:390px;width:420px;text-align:center;top:3185px;font-size:10.5px;line-height:18px;color:var(--ink-2)">Join the global leaders who trust WardPeak's unified platform for command, field operations, and back-office management.</p>
  <span class="btn btn-primary abs" style="left:433px;top:3252px;width:183px;height:38px">Schedule Enterprise Demo</span>
  <span class="btn btn-ghost abs" style="left:631px;top:3252px;width:134px;height:38px;font-size:11.5px">Contact Sales</span>
</section>

<footer class="footer abs">
  <div class="brand abs" style="left:206px;top:30px;font-size:9px"><span class="brand-mark" style="width:10px;height:10px"></span>WardPeak</div>
  <nav class="foot-links abs"><span>Privacy Policy</span><span>Terms of Service</span><span>Compliance</span><span>System Status</span></nav>
  <span class="copy abs">© 2024 WardPeak Enterprise Platform. All rights reserved.</span>
</footer>

</body>
</html>
```